company, product, services, opportunity presentation

Pelminor is a Payment Services Processor with value added product and services. We are focusing on the Payment Industry, Retail Merchants and Financial institutions. We have built total solution on AWS cloud to provide API based payment solutions such as Issuing of cards, Acquiring of payment transactions, Fraud prevention, Ecommerce, with customer facing APPs to provide dynamic virtual payment , 2FA and Passwordless sign in. Our focus is B2B .
We are developing our sales/investor pitch deck with slides covering company information, Market challengers (problems) that we are solving , Opportunities in the regional markets as well as global addressable Market for Payment cards. Pelminor Product and services offerings to meet these challenges and opportunities.
Total Addressable Market statistics and data. Specific to virtual payment cards, Second factor authentication and digital ID (passwordless). Primarily data and justification for reducing Ecommerce card abandonment and increasing Authorization rates
Pelminor Team and advisors’ slide. Current pipeline and customers. Use cases or case studies. Highlighting competitive advantage and USP. target clients and current pipline. Financials and projected spend in the next 2 years including target amount to raise fund. Solution and services slides and timeine of activities /roadmap
We need a PPT design to project better look and feel, crisp and eye catching graphic and design of the slides. clearer representation of key or salient points in all slides and information.

Target Market(s)

Financial Institutions, Retail (Merchants), Fintechs, Transportation

Industry/Entity Type

Cards and Payments Industry . Fraud prevention . Digital ID

Font styles to use
Sans Serif

Colors
F0912C
F2A743
F7CA91
FBE8D2
FDF5EE
EE7325
F08F49
F5BC92
FAE3D3
FDF4ED
A7469A
B969AE
D3A5CF
EDDBEB
F8F0F9
6B429C
8869AF
B7A5CE
E3DAEB
F3F0F8

Requirements
Must have
• problem to be solved, market challenges, market opportunities, product features and functionality. Use cases, Financial spend and funding. Team members and advisors. Timeline of roadmap for 2 years. competitive advantage and USP. Benefits to each customer segments
Nice to have
• Provision for future development on product and services. potentially covering other target markets such as Airlines, Insurance

```html
<!DOCTYPE html>
<html lang="en">
<head>
<meta charset="utf-8">
<title>Pelminor – Pitch Deck</title>
<link rel="stylesheet" href="https://fonts.googleapis.com/css2?family=Poppins:wght@400;500;600;700;800&display=swap">
<style>
:root{
  --orange:#EE7325;
  --orange-2:#F0912C;
  --orange-soft:#F7CA91;
  --orange-pale:#FBE8D2;
  --orange-mist:#FDF5EE;
  --purple:#6B429C;
  --plum:#A7469A;
  --plum-soft:#D3A5CF;
  --plum-pale:#F8F0F9;
  --lilac:#E3DAEB;
  --ink:#3a3a3a;
  --grey:#8a8a8a;
  --stage:#ececec;
}
*{box-sizing:border-box;margin:0;padding:0}
html,body{width:1200px;height:3884px;overflow:hidden}
body{background:var(--stage);font-family:'Poppins',sans-serif;color:var(--ink);position:relative}
.slide{position:absolute;left:88px;width:1024px;height:576px;background:#fff;overflow:hidden;box-shadow:0 4px 14px rgba(0,0,0,.12)}
.s1{top:48px}.s2{top:696px}.s3{top:1344px}.s4{top:1992px}.s5{top:2640px}.s6{top:3288px}
.brand{position:absolute;left:40px;top:26px;font-size:28px;font-weight:700;color:var(--purple);letter-spacing:-.5px}
.corner{position:absolute;right:0;top:0;width:0;height:0;border-top:46px solid var(--orange);border-left:46px solid transparent}
.slide-title{position:absolute;right:60px;top:30px;text-align:right;font-size:22px;font-weight:700;color:var(--purple);line-height:1.25}
.footer{position:absolute;left:40px;bottom:26px;display:flex;align-items:center;gap:6px;font-size:8px;color:var(--grey)}
.footer .dot{width:16px;height:16px;border:1.5px solid #666;border-radius:50%}
.footer .copy{margin-left:16px}
.page{position:absolute;right:40px;bottom:28px;font-size:8px;color:var(--grey)}
.photo{position:absolute}

/* slide 1 */
.hero-bar{position:absolute;left:22px;top:148px;width:6px;height:150px;background:var(--orange)}
.hero-title{position:absolute;left:40px;top:140px;font-size:40px;font-weight:700;line-height:1.2;color:var(--purple);width:480px}
.hero-title .hl{color:var(--orange)}

/* slide 2 */
.h-sub{position:absolute;left:40px;top:150px;font-size:24px;font-weight:700;color:var(--purple)}
.verticals{position:absolute;left:44px;top:200px;list-style:none;font-size:11px;line-height:1.7}
.verticals li::before{content:"";display:inline-block;width:7px;height:7px;background:var(--orange);margin-right:10px}
.verticals .sub{padding-left:20px}
.verticals .sub::before{background:var(--orange-soft)}
.solution-box{position:absolute;left:250px;top:222px;width:210px;height:130px;background:var(--plum-pale);border:1.5px solid var(--plum-soft);border-radius:10px;padding:12px 14px;text-align:center}
.solution-box h4{font-size:10px;font-weight:700;color:var(--purple);margin-bottom:6px}
.solution-box p{font-size:8px;color:var(--plum);line-height:1.5}
.screen{position:absolute;left:470px;top:150px;width:500px;height:290px;border:10px solid #e9e9e9;border-radius:10px;background:#fff}
.grid{width:100%;border-collapse:collapse;font-size:7px}
.grid th{background:var(--orange);color:#fff;font-weight:600;padding:6px 3px}
.grid td{border:1px solid var(--orange-pale);padding:6px 3px;text-align:center;color:var(--ink)}
.grid td.mark{width:40px}
.grid .mark span{display:inline-block;width:18px;height:11px;border-radius:2px;background:var(--orange-soft)}
.grid tr.band td{background:var(--purple);color:#fff;border-color:var(--purple)}
.grid tr.band2 td{background:var(--plum);color:#fff;border-color:var(--plum)}

/* slide 3 */
.ecosystem{position:absolute;left:50px;top:110px;width:924px;height:380px;border-radius:8px;background:linear-gradient(120deg,var(--orange-mist) 0%,var(--plum-pale) 55%,var(--lilac) 100%)}

/* slide 4 */
.problems{position:absolute;left:430px;top:180px;width:440px}
.problem{display:flex;align-items:center;gap:18px;margin-bottom:40px}
.tag{width:48px;height:34px;flex:none;background:var(--orange);clip-path:polygon(0 0,78% 0,100% 50%,78% 100%,0 100%);display:flex;align-items:center;justify-content:center;padding-right:8px}
.problem p{font-size:13px;font-weight:600;color:var(--ink);line-height:1.35}

/* slide 5 */
.notes{position:absolute;left:600px;top:130px;width:370px;list-style:none;font-size:9.5px;line-height:1.45;color:#555}
.notes li{margin-bottom:9px;padding-left:16px;position:relative}
.notes li::before{content:"";position:absolute;left:0;top:4px;width:7px;height:7px;border-radius:50%;background:var(--orange)}

/* slide 6 */
.contact{position:absolute;top:352px;width:160px;height:120px;background:var(--purple);color:#fff;text-align:center;padding-top:34px}
.contact .ico{position:absolute;left:62px;top:-18px;width:36px;height:36px;border-radius:50%;background:var(--orange);display:flex;align-items:center;justify-content:center}
.contact h5{font-size:13px;font-weight:700;margin-bottom:4px}
.contact p{font-size:8.5px;line-height:1.4;padding:0 12px}
</style>
</head>
<body>

<!-- Slide 1: cover -->
<section class="slide s1">
  <div class="brand">pelminor</div>
  <svg class="photo" style="left:500px;top:0" width="524" height="576" viewBox="0 0 524 576" role="img" aria-label="Photo of a man holding a payment card and a smartphone while shopping online">
    <defs>
      <linearGradient id="heroG" x1="0" y1="0" x2="1" y2="1">
        <stop offset="0" stop-color="#cfd6dc"/><stop offset=".55" stop-color="#8f9aa5"/><stop offset="1" stop-color="#4d5966"/>
      </linearGradient>
    </defs>
    <path d="M120 0 C60 120 70 260 150 360 C230 460 360 500 524 470 L524 0 Z" fill="#e6e6e6"/>
    <path d="M170 0 C110 110 120 240 200 330 C270 410 390 430 524 410 L524 0 Z" fill="url(#heroG)"/>
  </svg>
  <div class="hero-bar"></div>
  <h1 class="hero-title">Online Payment Security to <span class="hl">Eliminate Cart Abandonment</span></h1>
  <div class="footer"><span class="dot"></span><span class="dot"></span><span class="dot"></span><span class="dot"></span><span class="copy">© Copyright 2023 Company name. All Rights Reserved</span></div>
</section>

<!-- Slide 2: business solutions -->
<section class="slide s2">
  <div class="brand">pelminor</div>
  <div class="corner"></div>
  <h2 class="slide-title">Business Solutions &amp;<br>Client Verticals</h2>
  <h3 class="h-sub">Target Client Verticals</h3>
  <ul class="verticals">
    <li>Financial Institutions</li>
    <li class="sub">Issuers</li>
    <li class="sub">Acquirers</li>
    <li class="sub">Banks</li>
    <li class="sub">FinTechs</li>
    <li>Airlines</li>
    <li>Hotels</li>
    <li>Merchant Aggregators</li>
    <li>Large Retailers</li>
    <li>SMEs</li>
  </ul>
  <div class="solution-box">
    <h4>BUSINESS SOLUTIONS</h4>
    <p>Digital Payment Processing, Virtual Card Issuing, Acquiring Services, Fraud Prevention Engine, 2FA &amp; Passwordless Sign In, Ecommerce Gateway, Customer Apps and API Integration for Partners</p>
  </div>
  <div class="screen">
    <table class="grid">
      <tr><th>Segment</th><th>Issuing</th><th>Acquiring</th><th>Fraud</th><th>2FA</th><th>Cards</th></tr>
      <tr><td>Banks</td><td>Yes</td><td>Yes</td><td>Yes</td><td>Yes</td><td class="mark"><span></span></td></tr>
      <tr><td>FinTechs</td><td>Yes</td><td>No</td><td>Yes</td><td>Yes</td><td class="mark"><span></span></td></tr>
      <tr><td>Merchants</td><td>No</td><td>Yes</td><td>Yes</td><td>Yes</td><td class="mark"><span></span></td></tr>
      <tr><td>Airlines</td><td>No</td><td>Yes</td><td>Yes</td><td>No</td><td class="mark"><span></span></td></tr>
      <tr class="band"><td colspan="6">Cloud API Platform</td></tr>
      <tr class="band2"><td colspan="6">Digital ID &amp; Passwordless</td></tr>
      <tr class="band"><td colspan="6">Analytics &amp; Reporting</td></tr>
    </table>
  </div>
  <div class="footer"><span class="dot"></span><span class="dot"></span><span class="dot"></span><span class="dot"></span><span class="copy">© Copyright 2023 Company name. All Rights Reserved</span></div>
  <div class="page">PAGE 00 / 00</div>
</section>

<!-- Slide 3: ecosystem -->
<section class="slide s3">
  <div class="brand">pelminor</div>
  <div class="corner"></div>
  <h2 class="slide-title">Pelminor Payment<br>Ecosystem</h2>
  <div class="ecosystem" role="img" aria-label="Network diagram of the payment ecosystem linking acquirers, the cloud switching platform, partner institutions and merchants"></div>
  <div class="footer"><span class="dot"></span><span class="dot"></span><span class="dot"></span><span class="dot"></span><span class="copy">© Copyright 2023 Company name. All Rights Reserved</span></div>
  <div class="page">PAGE 00 / 00</div>
</section>

<!-- Slide 4: problem -->
<section class="slide s4">
  <div class="brand">pelminor</div>
  <div class="corner"></div>
  <h2 class="slide-title">Problem to Be Solved</h2>
  <svg class="photo" style="left:40px;top:110px" width="360" height="300" viewBox="0 0 360 300" role="img" aria-label="Photo of hands holding a smartphone and a payment card over a laptop">
    <defs><linearGradient id="probG" x1="0" y1="0" x2="1" y2="1"><stop offset="0" stop-color="#c7cfd8"/><stop offset="1" stop-color="#556270"/></linearGradient></defs>
    <rect width="360" height="300" rx="8" fill="url(#probG)"/>
  </svg>
  <div class="problems">
    <div class="problem"><div class="tag"><svg width="16" height="16" viewBox="0 0 16 16"><rect x="1" y="3" width="14" height="10" rx="2" fill="none" stroke="#fff" stroke-width="1.6"/><path d="M1 7h14" stroke="#fff" stroke-width="1.6"/></svg></div><p>Lorem ipsum dolor sit amet, consectetur<br>adipiscing elit, sed do eiusmod tempor</p></div>
    <div class="problem"><div class="tag"><svg width="16" height="16" viewBox="0 0 16 16"><path d="M2 3h2l2 8h7l2-6H5" fill="none" stroke="#fff" stroke-width="1.6"/><circle cx="7" cy="14" r="1.3" fill="#fff"/><circle cx="12" cy="14" r="1.3" fill="#fff"/></svg></div><p>Lorem ipsum dolor sit amet, consectetur<br>adipiscing elit, sed do eiusmod tempor</p></div>
    <div class="problem"><div class="tag"><svg width="16" height="16" viewBox="0 0 16 16"><rect x="3" y="7" width="10" height="8" rx="1.5" fill="#fff"/><path d="M5 7V5a3 3 0 016 0v2" fill="none" stroke="#fff" stroke-width="1.6"/></svg></div><p>Lorem ipsum dolor sit amet, consectetur<br>adipiscing elit, sed do eiusmod tempor</p></div>
  </div>
  <div class="footer"><span class="dot"></span><span class="dot"></span><span class="dot"></span><span class="dot"></span><span class="copy">© Copyright 2023 Company name. All Rights Reserved</span></div>
  <div class="page">PAGE 00 / 00</div>
</section>

<!-- Slide 5: market opportunities -->
<section class="slide s5">
  <div class="brand">pelminor</div>
  <div class="corner"></div>
  <h2 class="slide-title">Market Opportunities</h2>
  <svg style="position:absolute;left:30px;top:100px" width="540" height="380" viewBox="0 0 540 380" font-family="Poppins, sans-serif">
    <g stroke="#e3e3e3" stroke-width="1">
      <path d="M40 20H530M40 52H530M40 84H530M40 116H530M40 148H530M40 180H530M40 212H530M40 244H530M40 276H530M40 308H530"/>
    </g>
    <path d="M40 340H530" stroke="#999"/>
    <g font-size="8" fill="#666" text-anchor="end">
      <text x="32" y="23">100</text><text x="32" y="87">80</text><text x="32" y="151">60</text><text x="32" y="215">40</text><text x="32" y="279">20</text><text x="32" y="343">0</text>
    </g>
    <g fill="var(--orange-2)">
      <rect x="58" y="20" width="16" height="320"/><rect x="128" y="52" width="16" height="288"/><rect x="198" y="20" width="16" height="320"/><rect x="268" y="52" width="16" height="288"/><rect x="338" y="20" width="16" height="320"/><rect x="408" y="84" width="16" height="256"/><rect x="478" y="20" width="16" height="320"/>
    </g>
    <g fill="var(--purple)">
      <rect x="78" y="52" width="16" height="288"/><rect x="148" y="180" width="16" height="160"/><rect x="218" y="148" width="16" height="192"/><rect x="288" y="20" width="16" height="320"/><rect x="358" y="84" width="16" height="256"/><rect x="428" y="148" width="16" height="192"/><rect x="498" y="84" width="16" height="256"/>
    </g>
    <g font-size="7" fill="#555" text-anchor="middle">
      <text x="66" y="15">100</text><text x="86" y="47">90</text><text x="136" y="47">90</text><text x="156" y="175">50</text><text x="206" y="15">100</text><text x="226" y="143">60</text><text x="276" y="47">90</text><text x="296" y="15">100</text><text x="346" y="15">100</text><text x="366" y="79">80</text><text x="416" y="79">80</text><text x="436" y="143">60</text><text x="486" y="15">100</text><text x="506" y="79">80</text>
    </g>
    <g font-size="9" fill="#555" text-anchor="middle">
      <text x="76" y="358">Sun</text><text x="146" y="358">Mon</text><text x="216" y="358">Tue</text><text x="286" y="358">Wed</text><text x="356" y="358">Thu</text><text x="426" y="358">Fri</text><text x="496" y="358">Sat</text>
    </g>
  </svg>
  <ul class="notes">
    <li>Lorem ipsum dolor sit consectetur adipiscing elit, sed do eiusmod tempor incididunt ut labore et dolore magna aliqua.</li>
    <li>Lorem ipsum dolor sit consectetur adipiscing elit, sed do eiusmod.</li>
    <li>Lorem ipsum dolor sit consectetur adipiscing elit, sed do eiusmod tempor incididunt ut labore et dolore magna aliqua.</li>
    <li>Lorem ipsum dolor sit consectetur adipiscing elit, sed do eiusmod.</li>
    <li>Lorem ipsum dolor sit consectetur adipiscing elit, sed do eiusmod tempor incididunt ut labore et dolore magna aliqua.</li>
    <li>Lorem ipsum dolor sit consectetur adipiscing elit, sed do eiusmod.</li>
  </ul>
  <div class="footer"><span class="dot"></span><span class="dot"></span><span class="dot"></span><span class="dot"></span><span class="copy">© Copyright 2023 Company name. All Rights Reserved</span></div>
  <div class="page">PAGE 00 / 00</div>
</section>

<!-- Slide 6: thank you -->
<section class="slide s6">
  <div class="brand">pelminor</div>
  <div class="corner"></div>
  <h2 class="slide-title">Thankyou</h2>
  <svg class="photo" style="left:0;top:240px" width="1024" height="260" viewBox="0 0 1024 260" role="img" aria-label="Photo of a person paying online with a card at a laptop">
    <defs><linearGradient id="thxG" x1="0" y1="0" x2="1" y2="0"><stop offset="0" stop-color="#5d6a78"/><stop offset=".5" stop-color="#9aa4ae"/><stop offset="1" stop-color="#6f7b88"/></linearGradient></defs>
    <rect width="1024" height="260" fill="url(#thxG)"/>
  </svg>
  <div class="contact" style="left:222px">
    <div class="ico"><svg width="16" height="16" viewBox="0 0 16 16"><path d="M8 1a5 5 0 00-5 5c0 4 5 9 5 9s5-5 5-9a5 5 0 00-5-5z" fill="#fff"/><circle cx="8" cy="6" r="1.8" fill="var(--orange)"/></svg></div>
    <h5>Address :</h5>
    <p>NO. Lorem ipsum dolor sit amet, consectetur</p>
  </div>
  <div class="contact" style="left:432px">
    <div class="ico"><svg width="16" height="16" viewBox="0 0 16 16"><path d="M3 1h3l1.5 4-2 1.2a9 9 0 004.3 4.3L11 8.5l4 1.5v3a2 2 0 01-2 2A12 12 0 011 3a2 2 0 012-2z" fill="#fff"/></svg></div>
    <h5>Phone :</h5>
    <p>+1 000 000 0000</p>
  </div>
  <div class="contact" style="left:642px">
    <div class="ico"><svg width="16" height="16" viewBox="0 0 16 16"><rect x="1" y="3" width="14" height="10" rx="1.5" fill="#fff"/><path d="M1.5 4l6.5 5 6.5-5" fill="none" stroke="var(--orange)" stroke-width="1.4"/></svg></div>
    <h5>Email :</h5>
    <p>info@pelminor.com</p>
  </div>
  <div class="footer"><span class="dot"></span><span class="dot"></span><span class="dot"></span><span class="dot"></span><span class="copy">© Copyright 2023 Company name. All Rights Reserved</span></div>
  <div class="page">PAGE 00 / 00</div>
</section>

</body>
</html>
```